Perfume packaging design

We are a company producing perfumery and deodorants in the upper mass market segment (semi-selective). We need a packaging design for our new fragrance for women called Moon Petal. You will find attached a picture of the chosen bottle and cap along with specification.

The fragrance is modern and delicate. It is sweet with floral accent and notes of mandarin, rose, peach.

Suitable for evening perfume as well as casual daily.

Looking for:
1. logo - "Moon Petal" on bottle and packaging
2. Color of the perfume
3. Design of the carton box

Product is 100ml eau de perfume for women.

Target Market(s)

Target market is Eastern Europe and middle east

Women
Age 30-45
Price range - semi-selective
Sales channels - perfumeries, drug stores and online

Industry/Entity Type

It Company

Requirements
Must have
• Packaging - carton
Perfume should be colored
Embosing
Nice to have
• Golden hot stamping or other golden element

```html
<!DOCTYPE html>
<html lang="en">
<head>
<meta charset="utf-8">
<title>Moon Petal – Carton Dieline</title>
<link href="https://fonts.googleapis.com/css2?family=Open+Sans:wght@400;600&display=swap" rel="stylesheet">
<style>
  :root {
    --paper: #ffffff;
    --cut-line: #4a4a4a;
    --sage: #b7c6b5;
    --sage-deep: #a3b49f;
    --rose: #d9b1a6;
    --cocoa: #4a3430;
    --blush-band: #c9a096;
    --gold-light: #f6d77a;
    --gold-deep: #c8901c;
    --ink-light: #ffffff;
  }
  * { margin: 0; padding: 0; box-sizing: border-box; }
  html, body { width: 1200px; height: 1000px; overflow: hidden; background: var(--paper); }
  .dieline { position: relative; width: 1200px; height: 1000px; font-family: "Open Sans", Arial, sans-serif; color: var(--ink-light); }
  .dieline__art { position: absolute; inset: 0; }
  .panel-text { position: absolute; text-align: center; }
  .copy-block {
    left: 420px; top: 529px; width: 158px;
    font-size: 7.6px; line-height: 10px;
  }
  .brand-name {
    left: 900px; top: 516px; width: 240px;
    font-size: 22px; font-weight: 400; letter-spacing: 0.5px; line-height: 30px;
  }
  .variant-label {
    left: 900px; top: 658px; width: 240px;
    font-size: 7.5px; line-height: 10px; letter-spacing: 0.3px;
  }
  .volume { top: 725px; font-size: 8px; }
  .volume--ml { left: 904px; }
  .volume--oz { left: 1096px; width: 38px; text-align: right; }
</style>
</head>
<body>
<main class="dieline">
  <svg class="dieline__art" width="1200" height="1000" viewBox="0 0 1200 1000">
    <defs>
      <linearGradient id="floral-tone" x1="0" y1="0" x2="1" y2="1">
        <stop offset="0" stop-color="var(--sage)"/>
        <stop offset="0.5" stop-color="var(--rose)" stop-opacity="0.9"/>
        <stop offset="1" stop-color="var(--sage-deep)"/>
      </linearGradient>
      <linearGradient id="gold-foil" x1="0" y1="0" x2="1" y2="0">
        <stop offset="0" stop-color="var(--gold-deep)"/>
        <stop offset="0.5" stop-color="var(--gold-light)"/>
        <stop offset="1" stop-color="var(--gold-deep)"/>
      </linearGradient>
    </defs>

    <g class="carton-flaps" role="img" aria-label="Vintage floral print of pink roses and green leaves on a sage background" fill="url(#floral-tone)" stroke="var(--cut-line)" stroke-width="0.9">
      <polygon class="tuck-flap" points="369,160 392,82 602,82 629,160"/>
      <rect class="lid-panel" x="369" y="160" width="260" height="263"/>
      <polygon class="dust-flap dust-flap--left" points="316,187 369,160 369,423 316,395"/>
      <polygon class="dust-flap dust-flap--right" points="629,160 682,187 682,395 629,423"/>
      <polygon class="glue-flap" points="50,435 104,423 104,750 50,738"/>
      <rect class="side-panel" x="104" y="423" width="265" height="327"/>
      <rect class="back-panel" x="369" y="423" width="260" height="327"/>
      <rect class="side-panel" x="629" y="423" width="261" height="327"/>
      <rect class="front-panel" x="890" y="423" width="260" height="327"/>
      <polygon class="bottom-flap" points="104,750 369,750 270,830 337,883 130,883 182,830"/>
      <polygon class="bottom-flap" points="369,750 629,750 629,883 529,883 529,830 447,830 447,883 369,883"/>
      <polygon class="bottom-flap" points="629,750 890,750 795,830 865,883 655,883 708,830"/>
      <polygon class="bottom-flap" points="890,750 1150,750 1150,883 1050,883 1050,830 968,830 968,883 890,883"/>
    </g>

    <g class="label-boxes" fill="var(--cocoa)">
      <rect x="115" y="433" width="240" height="305"/>
      <rect x="376" y="430" width="247" height="312"/>
      <rect x="900" y="433" width="240" height="305"/>
    </g>

    <g class="wrap-band">
      <rect x="104" y="652" width="1046" height="5" fill="url(#gold-foil)"/>
      <rect x="104" y="657" width="1046" height="22" fill="var(--blush-band)"/>
    </g>

    <g class="gold-ornaments" fill="url(#gold-foil)" opacity="0.55">
      <rect x="425" y="490" width="148" height="28" rx="14" role="img" aria-label="Gold scroll ornament"/>
      <rect x="945" y="474" width="150" height="40" rx="16" role="img" aria-label="Gold scroll ornament above the name"/>
      <rect x="945" y="549" width="150" height="42" rx="16" role="img" aria-label="Gold scroll ornament below the name"/>
    </g>
  </svg>

  <p class="panel-text copy-block">Lorem ipsum dolor sit amet, consectetur adipisicing elit, sed do eiusmod tempor incididunt ut labore et dolore magna aliqua. Ut enim ad minim veniam, quis nostrud exercitation ullamco laboris nisi ut aliquip ex ea commodo consequat. Duis aute irure dolor in reprehenderit in voluptate velit esse cillum dolore eu fugiat nulla pariatur. Excepteur sint occaecat cupidatat non proident, sunt in culpa qui officia deserunt mollit anim id est laborum.</p>

  <h1 class="panel-text brand-name">Moon Petal</h1>
  <p class="panel-text variant-label">EAU DE PARFUM<br>NATURAL SPRAY</p>
  <p class="panel-text volume volume--ml">100ml</p>
  <p class="panel-text volume volume--oz">3.4 fl oz</p>
</main>
</body>
</html>
```